Unique business card design

Boutique coastal hotel suites - in need of clever stand out business card I have uploaded the logo that I had created through quill forge I want something that is clever and stands out from everyone else - 418 Brantwell Avenue Tessick Bay Northmark 99571 phone or text 907 -581-6142 www.primemarrowbysuites.com

Target Market(s)

Men and woman

Industry/Entity Type

Boutique coastal hotel

Contact Information for Business Card

Marrowby Suites Tessick Bay Northmark marrowby_suites@mailnest.net

Requirements
Must have
• Classy - clever -bold 907-581-6142 call or text

```html
<!DOCTYPE html>
<html lang="en">
<head>
<meta charset="utf-8">
<title>Marrowby Suites – Business Card</title>
<link rel="stylesheet" href="https://fonts.googleapis.com/css2?family=Montserrat:wght@400;500;600&display=swap">
<style>
  :root {
    --backdrop: #ece8e2;
    --card-white: #ffffff;
    --ink: #1e1e1e;
    --ink-soft: #333333;
    --muted: #777777;
    --band: #1f1f1f;
    --accent: #c8283a;
    --rule: #3b4a5e;
  }
  * { margin: 0; padding: 0; box-sizing: border-box; }
  html, body {
    width: 1200px; height: 1092px; overflow: hidden;
    background: var(--backdrop);
    font-family: "Montserrat", Arial, sans-serif;
  }
  .canvas { position: relative; width: 1200px; height: 1092px; }

  .card {
    position: absolute;
    width: 620px; height: 354px;
    background: var(--card-white);
    box-shadow: 0 10px 28px rgba(0,0,0,0.18);
    overflow: hidden;
  }
  .card--front { left: 70px; top: 100px; }
  .card--back  { left: 510px; top: 620px; }

  /* wordmark: name with one square, rule underneath */
  .wordmark {
    display: inline-flex; align-items: center; gap: 10px;
    color: var(--ink);
    font-weight: 600;
    letter-spacing: 3px;
    white-space: nowrap;
    border-bottom: 2px solid var(--rule);
  }
  .wordmark__square { background: var(--accent); flex: none; }

  .card--front .wordmark {
    position: absolute; left: 38px; top: 60px;
    font-size: 22px; padding-bottom: 8px;
  }
  .card--front .wordmark__square { width: 12px; height: 12px; }

  .contact {
    position: absolute; left: 340px; top: 118px;
    list-style: none;
    color: var(--ink-soft);
    font-size: 15px; line-height: 1.4;
  }
  .contact li { display: flex; align-items: flex-start; gap: 12px; margin-bottom: 10px; }
  .contact svg { width: 16px; height: 16px; flex: none; margin-top: 3px; fill: var(--ink); }
  .contact .phone { font-weight: 600; color: var(--ink); }

  .person { position: absolute; left: 120px; top: 258px; text-align: right; }
  .person__name { font-size: 21px; font-weight: 500; color: var(--ink-soft); }
  .person__name strong { font-weight: 600; }
  .person__tagline { font-size: 10px; color: var(--muted); margin-top: 1px; }

  /* back */
  .band { position: absolute; left: 0; width: 100%; background: var(--band); }
  .band--top { top: 0; height: 96px; }
  .band--bottom { bottom: 0; height: 96px; }
  .card--back .wordmark {
    position: absolute; left: 50%; top: 50%;
    transform: translate(-50%, -50%);
    font-size: 30px; padding-bottom: 10px;
  }
  .card--back .wordmark__square { width: 15px; height: 15px; }
</style>
</head>
<body>
<main class="canvas">

  <section class="card card--front" aria-label="Business card front">
    <div class="wordmark"><span class="wordmark__square"></span>MARROWBY SUITES</div>

    <ul class="contact">
      <li>
        <svg viewBox="0 0 16 16" aria-hidden="true"><path d="M8 1 1 7.5h2V15h4v-4h2v4h4V7.5h2z"/></svg>
        <span>418 Brantwell Avenue<br>Tessick Bay Northmark 99571</span>
      </li>
      <li>
        <svg viewBox="0 0 16 16" aria-hidden="true"><path d="M3.6 1.2 6 3.8 4.7 5.8c.9 2 2.5 3.6 4.5 4.5l2-1.3 2.6 2.4-1.3 2.4C7.4 13.6 2.4 8.6 1.2 3.5z"/></svg>
        <span class="phone">(907 ) -581-6142</span>
      </li>
      <li>
        <svg viewBox="0 0 16 16" aria-hidden="true"><path d="M1 3h14v10H1zm1.5 1.3v.4L8 8.6l5.5-3.9v-.4zM2.5 6.3v5.4h11V6.3L8 10.2z"/></svg>
        <span>marrowby_suites@mailnest.net</span>
      </li>
    </ul>

    <div class="person">
      <div class="person__name">Your <strong>NAME</strong></div>
      <div class="person__tagline">Tagline here</div>
    </div>
  </section>

  <section class="card card--back" aria-label="Business card back">
    <div class="band band--top"></div>
    <div class="wordmark"><span class="wordmark__square"></span>MARROWBY SUITES</div>
    <div class="band band--bottom"></div>
  </section>

</main>
</body>
</html>
```